Kestrel Motorworks Card

Our company is an offroad fabrication shop that does everything from product installs to complete turnkey offroad racers. We are looking to generate new business cards for the 2014 Lords of the Canyon race in February. This is one of the largest offroad races in the country. We would like to see designs that incorporate the colors used in our logo - black, red, and white.

Industry/Entity Type

Shop

Contact Information for Business Card

KESTREL Motorworks, 2873 Marwood Ln. Houston, TX, 713-452-3071, www.kestrelmotorworks.example, Leon Farrowby, Owen Tilsley, Owners.

Requirements
Nice to have
• Would like to see the Logo full size on the back size of the car.

```html
<!DOCTYPE html>
<html lang="en">
<head>
<meta charset="utf-8">
<title>Kestrel Motorworks – Business Card</title>
<link rel="stylesheet" href="https://fonts.googleapis.com/css2?family=Saira+Condensed:wght@500;600;700;800&display=swap">
<style>
  :root {
    --board: #ececec;
    --card: #000000;
    --red: #e11a1a;
    --white: #ffffff;
    --label: #111111;
    --font: "Saira Condensed", "Arial Narrow", sans-serif;
  }
  * { box-sizing: border-box; margin: 0; padding: 0; }
  html, body { width: 1200px; height: 808px; overflow: hidden; background: var(--board); }
  .board { position: relative; width: 1200px; height: 808px; background: var(--board); font-family: var(--font); }

  .side-label { position: absolute; font-weight: 700; font-size: 38px; color: var(--label); line-height: 1; }
  .side-label--front { left: 55px; top: 80px; }
  .side-label--back { left: 1000px; top: 318px; }

  .card { position: absolute; width: 520px; height: 298px; background: var(--card); overflow: hidden; box-shadow: 0 10px 24px rgba(0,0,0,.25); }
  .card--front { left: 110px; top: 140px; }
  .card--back { left: 600px; top: 440px; }

  .card__band { position: absolute; left: 0; right: 0; bottom: 0; height: 6px; background: var(--red); }
  .card__band::after { content: ""; position: absolute; right: 0; top: 0; width: 60px; height: 100%; background: var(--white); }
  .card__band::before { content: ""; position: absolute; right: 60px; top: 0; width: 12px; height: 100%; background: var(--card); }

  /* Front */
  .brand-mark { position: absolute; left: 0; right: 0; top: 0; bottom: 6px; display: flex; align-items: center; justify-content: center; gap: 18px; }
  .brand-mark__dot { width: 26px; height: 26px; border-radius: 50%; background: var(--red); }
  .brand-mark__name { font-weight: 800; font-size: 50px; color: var(--red); letter-spacing: 1px; line-height: 1; }

  /* Back */
  .back-title { position: absolute; left: 0; right: 0; top: 26px; text-align: center; font-weight: 700; font-size: 30px; color: var(--white); line-height: 1; }
  .accent { color: var(--red); }

  .owner { position: absolute; width: 175px; }
  .owner--left { left: 52px; top: 94px; }
  .owner--right { left: 282px; top: 78px; }
  .owner__name { font-weight: 700; font-size: 22px; color: var(--white); line-height: 1.1; white-space: nowrap; }
  .owner__rule { height: 2px; margin-top: 4px; }
  .owner--left .owner__rule { background: var(--red); }
  .owner--right .owner__rule { background: var(--white); }
  .owner__role { text-align: right; font-size: 10px; font-weight: 600; color: var(--white); margin-top: 2px; }

  .contact { position: absolute; font-size: 10px; font-weight: 600; color: var(--white); text-align: center; line-height: 1.6; white-space: nowrap; }
  .contact--web { left: 40px; top: 218px; width: 160px; }
  .contact--phone { left: 210px; top: 178px; width: 130px; }
  .contact--address { left: 340px; top: 152px; width: 170px; }
  .contact__icon { display: block; margin: 0 auto 6px; }
</style>
</head>
<body>
<main class="board">
  <p class="side-label side-label--front">Front side</p>
  <p class="side-label side-label--back">Back side</p>

  <section class="card card--front" aria-label="Card front">
    <div class="brand-mark">
      <span class="brand-mark__dot"></span>
      <span class="brand-mark__name">KESTREL Motorworks</span>
    </div>
    <div class="card__band"></div>
  </section>

  <section class="card card--back" aria-label="Card back">
    <h1 class="back-title">KESTREL <span class="accent">Motorworks</span></h1>

    <div class="owner owner--left">
      <p class="owner__name">Leon <span class="accent">Farrowby</span></p>
      <div class="owner__rule"></div>
      <p class="owner__role">Owner</p>
    </div>

    <div class="owner owner--right">
      <p class="owner__name">Owen <span class="accent">Tilsley</span></p>
      <div class="owner__rule"></div>
      <p class="owner__role">Owner</p>
    </div>

    <div class="contact contact--web">
      <p>Website</p>
      <p>www.kestrelmotorworks.example</p>
    </div>

    <div class="contact contact--phone">
      <svg class="contact__icon" width="14" height="18" viewBox="0 0 14 18" aria-hidden="true">
        <rect x="2" y="1" width="10" height="16" rx="1.5" fill="none" stroke="#fff" stroke-width="1.2"/>
        <line x1="5" y1="14.5" x2="9" y2="14.5" stroke="#fff" stroke-width="1.2"/>
      </svg>
      <p>phone : 713-452-3071</p>
    </div>

    <div class="contact contact--address">
      <svg class="contact__icon" width="20" height="16" viewBox="0 0 20 16" aria-hidden="true">
        <path d="M2 8 L10 1 L18 8 M4 7 V15 H16 V7" fill="none" stroke="#fff" stroke-width="1.2" stroke-linejoin="round"/>
      </svg>
      <p>Address : 2873 Marwood Ln. Houston, TX</p>
    </div>

    <div class="card__band"></div>
  </section>
</main>
</body>
</html>
```